Business Card Design Project

Colette Marvaux logo on front of card with 'of Sydney' added in small font.
Back of card needs to include the following information :

"Pure pleasure for the discerning gentleman" (I may omit once I've seen the design)

colettemarvaux.com.au

Contact by SMS or email only :

colette@colettemarvaux.com.au
Mobile : 0483 615 204 or + 61 483 615 204

Target Market(s)

Male professionals aged 20-60.

Industry/Entity Type

Business

Requirements
Must have
• Simple, bold, stylish and elegant.

```html
<!DOCTYPE html>
<html lang="en">
<head>
<meta charset="utf-8">
<title>Colette Marvaux – Business Card</title>
<link rel="stylesheet" href="https://fonts.googleapis.com/css2?family=Alegreya+Sans:wght@300;400&family=Yellowtail&display=block">
<style>
  :root {
    --stage: #3a3f4a;
    --ink: #000000;
    --paper: #ffffff;
    --ghost: rgba(128, 128, 128, 0.5);
    --script: "Yellowtail", "Brush Script MT", "Segoe Script", cursive;
    --sans: "Alegreya Sans", "Helvetica Neue", Arial, sans-serif;
  }
  html, body {
    margin: 0;
    padding: 0;
    width: 1200px;
    height: 900px;
    overflow: hidden;
    background: var(--stage);
  }
  .card {
    position: absolute;
    top: 309px;
    width: 564px;
    height: 406px;
    border-radius: 9px;
    overflow: hidden;
  }
  .card--back { left: 25px; background: var(--paper); }
  .card--front { left: 605px; background: var(--ink); }

  .back-wave { position: absolute; inset: 0; }

  .tagline {
    position: absolute;
    top: 30px;
    left: 0;
    width: 100%;
    margin: 0;
    padding-right: 30px;
    box-sizing: border-box;
    text-align: center;
    font-family: var(--script);
    font-weight: 400;
    font-size: 23px;
    line-height: 1.2;
    color: var(--ink);
  }
  .ghost-name {
    position: absolute;
    left: 40px;
    top: 30px;
    margin: 0;
    font-family: var(--sans);
    font-weight: 300;
    font-size: 150px;
    line-height: 1;
    color: var(--ghost);
    white-space: nowrap;
  }
  .contact {
    position: absolute;
    left: 290px;
    right: 14px;
    top: 252px;
    color: var(--paper);
  }
  .contact__label {
    margin: 0 0 0 48px;
    font-family: var(--script);
    font-weight: 400;
    font-size: 14px;
    line-height: 1.2;
  }
  .contact__note {
    margin: 18px 0 10px 48px;
    font-family: var(--script);
    font-weight: 400;
    font-size: 13px;
    line-height: 1.2;
  }
  .contact__lines {
    margin: 0;
    text-align: right;
    font-family: var(--sans);
    font-weight: 300;
    font-size: 16px;
    line-height: 16px;
  }
  .contact__web {
    margin: 12px 0 0;
    text-align: right;
    font-family: var(--script);
    font-weight: 400;
    font-size: 19px;
    line-height: 1.2;
    white-space: nowrap;
  }

  .brand {
    position: absolute;
    top: 172px;
    left: 0;
    width: 100%;
    margin: 0;
    text-align: center;
    font-family: var(--sans);
    font-weight: 300;
    font-size: 40px;
    letter-spacing: 5px;
    color: var(--paper);
  }
  .locale {
    position: absolute;
    right: 20px;
    bottom: 18px;
    margin: 0;
    font-family: var(--script);
    font-weight: 400;
    font-size: 17px;
    line-height: 1.2;
    color: var(--paper);
  }
  .edge-tab {
    position: absolute;
    right: 3px;
    bottom: 13px;
    width: 12px;
    height: 31px;
    background: var(--paper);
  }
</style>
</head>
<body>
  <section class="card card--back" aria-label="Card back">
    <svg class="back-wave" width="564" height="406" viewBox="0 0 564 406" aria-hidden="true">
      <path d="M0 154 Q282 66 564 154 L564 406 L0 406 Z" fill="#000"/>
    </svg>
    <p class="ghost-name" aria-hidden="true">Colette</p>
    <h2 class="tagline">Pure pleasure for the discerning gentleman</h2>
    <div class="contact">
      <p class="contact__label">Contacts:</p>
      <p class="contact__note">Contact by SMS or email only</p>
      <p class="contact__lines">0483 615 204<br>+ 61 483 615 204<br>colette@colettemarvaux.com.au</p>
      <p class="contact__web">web: colettemarvaux.com.au</p>
    </div>
  </section>

  <section class="card card--front" aria-label="Card front">
    <h1 class="brand">Colette Marvaux</h1>
    <p class="locale">of Sydney</p>
    <span class="edge-tab" aria-hidden="true"></span>
  </section>
</body>
</html>
```